Design some Business Cards

Hi everyone! I need a business card. I post the infos in the file attached. The style must be easy but effective, white background and black writing. In addition i would like to have an arrow (symbol of import-export) with the colours of green, white and red (italian flag). I attach an example. My only problem is the iranian number, i will have it next week. I post the contest now because in Iran this site is banned, so if i can find something interesting i would like to have the Word file and i will put the number by myself next week. Good luck ;)

```html
<!DOCTYPE html>
<html lang="en">
<head>
<meta charset="utf-8">
<title>Business Card – Darius Kaveh</title>
<link rel="stylesheet" href="https://fonts.googleapis.com/css2?family=Poppins:wght@400;600&display=swap">
<style>
  :root {
    --backdrop: #e6e6e6;
    --card: #ffffff;
    --ink: #1d1d1d;
    --ink-soft: #444444;
    --green: #3ea653;
    --red: #d9403a;
  }
  * { box-sizing: border-box; margin: 0; padding: 0; }
  html, body {
    width: 1200px; height: 749px; overflow: hidden;
    background: var(--backdrop);
    font-family: "Poppins", sans-serif;
    color: var(--ink);
  }
  .business-card {
    position: absolute;
    left: 170px; top: 134px;
    width: 860px; height: 480px;
    background: var(--card);
    box-shadow: 0 6px 24px rgba(0,0,0,0.12);
    overflow: hidden;
  }
  .card-title {
    position: absolute; top: 92px; left: 0; right: 0;
    display: flex; justify-content: center; align-items: center; gap: 16px;
  }
  .card-title .name {
    font-weight: 600; font-size: 36px; letter-spacing: 0.2px;
  }
  .chevrons { width: 40px; height: 22px; }
  .contact {
    position: absolute;
    display: flex; flex-direction: column; align-items: center; gap: 10px;
    font-size: 15px; line-height: 1.45; color: var(--ink-soft);
  }
  .contact svg { width: 22px; height: 22px; fill: var(--ink); }
  .contact-phone { left: 70px; bottom: 54px; align-items: flex-start; }
  .contact-phone svg { margin-left: 40px; }
  .contact-email { left: 0; right: 0; bottom: 108px; }
  .contact-address { right: 60px; bottom: 52px; text-align: center; }
  .phone-pending {
    display: inline-block; width: 110px;
    border-bottom: 1px dashed var(--ink-soft); vertical-align: middle;
  }
  .band { position: absolute; bottom: 0; height: 16px; }
  .band-green { left: 0; width: 40%; background: var(--green); }
  .band-red { right: 0; width: 30%; background: var(--red); }
</style>
</head>
<body>
  <main class="business-card">
    <header class="card-title">
      <svg class="chevrons" viewBox="0 0 40 22" aria-hidden="true">
        <polyline points="3,3 11,11 3,19" fill="none" stroke="var(--green)" stroke-width="4"/>
        <polyline points="17,3 25,11 17,19" fill="none" stroke="var(--red)" stroke-width="4"/>
      </svg>
      <h1 class="name">Eng. Darius Kaveh</h1>
      <svg class="chevrons" viewBox="0 0 40 22" aria-hidden="true">
        <polyline points="23,3 15,11 23,19" fill="none" stroke="var(--red)" stroke-width="4"/>
        <polyline points="37,3 29,11 37,19" fill="none" stroke="var(--green)" stroke-width="4"/>
      </svg>
    </header>

    <div class="contact contact-phone">
      <svg viewBox="0 0 24 24" aria-hidden="true">
        <path d="M7 1h10a2 2 0 0 1 2 2v18a2 2 0 0 1-2 2H7a2 2 0 0 1-2-2V3a2 2 0 0 1 2-2zm0 3v14h10V4H7zm5 15.5a1.2 1.2 0 1 0 0 2.4 1.2 1.2 0 0 0 0-2.4z"/>
      </svg>
      <p>Italy: +39 320 555 0147<br>Iran: +98 <span class="phone-pending"></span></p>
    </div>

    <div class="contact contact-email">
      <svg viewBox="0 0 24 24" aria-hidden="true">
        <path d="M2 5h20v14H2V5zm2 2v.6l8 5.2 8-5.2V7H4z"/>
      </svg>
      <p>darius.kaveh@mailbox.com</p>
    </div>

    <div class="contact contact-address">
      <svg viewBox="0 0 24 24" aria-hidden="true">
        <path d="M12 1a7 7 0 0 0-7 7c0 5.3 7 15 7 15s7-9.7 7-15a7 7 0 0 0-7-7zm0 9.5A2.5 2.5 0 1 1 12 5.5a2.5 2.5 0 0 1 0 5z"/>
      </svg>
      <p>Second Floor n. 118, Sepid Tower,<br>Tehran, Iran</p>
    </div>

    <div class="band band-green"></div>
    <div class="band band-red"></div>
  </main>
</body>
</html>
```